Home Staging Company needs business card design

We're a home staging company called Brightly Settled Home Staging. We would like a business card design that includes aqua and gray. Our current logo of house within chair is fine but I find we almost always use the logo in one color. I'll upload images of front and back of our current card and our logo. Note that we have dropped "Solutions" from our company name and don't want to include it on the card.

Target Market(s)

Realtors and homeowners - people interested in selling their homes

Contact Information for Business Card

Marisol Vantrease
Brightly Settled Home Staging
612-348-9071
www.brightlysettled.example
marisol@brightlysettled.example

Font styles to use
Serif
Script

Requirements
Must have
• My logo and contact details
• UPDATE***
• I forgot to say that the company name should be included on the front of the card somehow.

```html
<!DOCTYPE html>
<html lang="en">
<head>
<meta charset="utf-8">
<title>Brightly Settled Home Staging — Business Card</title>
<link rel="stylesheet" href="https://fonts.googleapis.com/css2?family=Playfair+Display:wght@400&family=Jost:wght@400&display=swap">
<style>
  :root {
    --stage: #3a3a3a;
    --card-dark: #1e1e1e;
    --card-aqua: #4abfbc;
    --aqua: #4abfbc;
    --white: #ffffff;
    --shadow: rgba(0, 0, 0, 0.35);
  }
  * { box-sizing: border-box; margin: 0; padding: 0; }
  html, body {
    width: 1200px;
    height: 650px;
    overflow: hidden;
    background: var(--stage);
  }
  .stage {
    position: relative;
    width: 1200px;
    height: 650px;
    display: flex;
    align-items: center;
    justify-content: center;
    gap: 60px;
  }
  .card {
    width: 510px;
    height: 300px;
    border-radius: 3px;
    box-shadow: 0 14px 30px var(--shadow);
    display: flex;
    flex-direction: column;
    align-items: center;
    justify-content: center;
    text-align: center;
    color: var(--white);
  }
  .card--back { background: var(--card-dark); }
  .card--front { background: var(--card-aqua); }

  .brand {
    display: flex;
    align-items: center;
    gap: 14px;
    font-family: "Playfair Display", Georgia, serif;
    font-weight: 400;
    line-height: 1.1;
  }
  .brand__mark {
    border-radius: 50%;
    flex: none;
  }
  .card--back .brand { color: var(--aqua); font-size: 22px; margin-bottom: 26px; }
  .card--back .brand__mark { width: 52px; height: 52px; background: var(--aqua); }
  .brand__name { text-align: left; }

  .card--front .brand {
    flex-direction: column;
    gap: 14px;
    font-size: 28px;
    color: var(--white);
  }
  .card--front .brand__mark { width: 70px; height: 70px; background: var(--white); }
  .card--front .brand__name { text-align: center; }

  .contact__name {
    font-family: "Playfair Display", Georgia, serif;
    font-variant: small-caps;
    font-size: 19px;
    letter-spacing: 0.06em;
    margin-bottom: 14px;
  }
  .contact__line {
    font-family: "Jost", "Futura", Arial, sans-serif;
    font-size: 14.5px;
    line-height: 1.35;
    letter-spacing: 0.02em;
  }
  .social {
    display: flex;
    gap: 10px;
    margin-top: 14px;
  }
  .social__dot {
    width: 10px;
    height: 10px;
    border-radius: 50%;
    background: var(--aqua);
  }
  .front__web {
    font-family: "Jost", "Futura", Arial, sans-serif;
    font-size: 12px;
    letter-spacing: 0.04em;
    margin-top: 36px;
  }
</style>
</head>
<body>
<main class="stage">
  <section class="card card--back" aria-label="Card back with contact details">
    <div class="brand">
      <span class="brand__mark" aria-hidden="true"></span>
      <span class="brand__name">Brightly Settled<br>Home Staging</span>
    </div>
    <p class="contact__name">Marisol Vantrease</p>
    <p class="contact__line">612-348-9071</p>
    <p class="contact__line">marisol@brightlysettled.example</p>
    <p class="contact__line">www.brightlysettled.example</p>
    <div class="social" aria-label="Social profiles">
      <span class="social__dot"></span>
      <span class="social__dot"></span>
      <span class="social__dot"></span>
    </div>
  </section>

  <section class="card card--front" aria-label="Card front with company name">
    <div class="brand">
      <span class="brand__mark" aria-hidden="true"></span>
      <span class="brand__name">Brightly Settled<br>Home Staging</span>
    </div>
    <p class="front__web">www.brightlysettled.example</p>
  </section>
</main>
</body>
</html>
```